2367 Halvorsen Avenue Medical Centre

We are looking for a design for new medical clinic.
We are accepting new patients at this new medical centre grand opening. Walk-ins are welcome.
Our cardiac and vascular surgical specialists are department heads at St Alder's Hospital, a leading teaching hospital in Toronto. These specialists will see cardiovascular consults are well as pre-surgical and post-surgical consultations and follow-ups.
Our lab is affiliated with several nuclear medicine clinics in the GTA.
Our Services Includes:
Family Practice
Cardiology Diagnostics
Cardiac & Vascular Surgical Consultation
Ultrasound & Vascular Testing
Open 6 days a week.
Ample Free Parking
Friendly Staffs

Target Market(s)

New Patients. Families of any age. Ethnic groups including Asians & Africans.

Industry/Entity Type

Medical

Font styles to use
Serif
Sans Serif
Decorative
Script
Other font styles liked:
• Arial calibri, verdana

Requirements
Must have
• Address:
• 2367 Halvorsen Avenue East
• Unit 225
• Scarborough, Ontario
• K7T 2P4
• Tel: (416) 555-0148
Nice to have
• Caring and inviting environment.
• Simple but classy.
• Standout colors.
Should not have
• Busy images. Aside from this, any ideas are welcome.

```html
<!DOCTYPE html>
<html lang="en">
<head>
<meta charset="utf-8">
<title>Halvorsen Avenue Medical Clinic — Now Open</title>
<link href="https://fonts.googleapis.com/css2?family=Montserrat:wght@700;800;900&family=Roboto+Slab:wght@400;700&display=swap" rel="stylesheet">
<style>
  :root {
    --clinic-blue: #1a55e3;
    --sky-blue: #3db4f0;
    --teal: #17a090;
    --alert-red: #d3111b;
    --ink: #111111;
    --white: #ffffff;
  }
  html, body {
    margin: 0;
    padding: 0;
    overflow: hidden;
    background: var(--white);
  }
  p, h1, h2, ul { margin: 0; padding: 0; }
  .flyer {
    position: relative;
    width: 934px;
    height: 1200px;
    overflow: hidden;
    background: var(--white);
    font-family: "Roboto Slab", Georgia, serif;
  }
  .hero-art {
    position: absolute;
    left: 0;
    top: 0;
    width: 934px;
    height: 640px;
  }
  .ribbon {
    position: absolute;
    left: -70px;
    top: 62px;
    width: 420px;
    height: 58px;
    background: var(--alert-red);
    transform: rotate(-35deg);
    transform-origin: center;
    display: flex;
    align-items: center;
    justify-content: center;
    color: var(--white);
    font-family: "Montserrat", Arial, sans-serif;
    font-weight: 800;
    font-size: 34px;
    letter-spacing: 1px;
  }
  .brand-mark {
    position: absolute;
    left: 186px;
    top: 150px;
    width: 120px;
    height: 120px;
    background: var(--alert-red);
  }
  .clinic-name {
    position: absolute;
    left: 360px;
    top: 118px;
    width: 540px;
    text-align: center;
    color: var(--clinic-blue);
    font-family: "Montserrat", Arial, sans-serif;
    font-weight: 900;
    line-height: 1;
  }
  .clinic-name .street { display: block; font-size: 34px; letter-spacing: 0.5px; }
  .clinic-name .word-medical { display: block; font-size: 104px; letter-spacing: -2px; margin-top: 4px; }
  .clinic-name .word-clinic { display: block; font-size: 104px; letter-spacing: -2px; margin-top: -18px; }
  .headline {
    position: absolute;
    left: 0;
    top: 638px;
    width: 904px;
    text-align: center;
    color: var(--alert-red);
    font-weight: 700;
    line-height: 1;
  }
  .headline .days { display: block; font-size: 54px; line-height: 54px; }
  .headline .walk-in { display: block; font-size: 31px; line-height: 31px; margin-top: 6px; }
  .services {
    position: absolute;
    left: 233px;
    top: 739px;
    color: var(--ink);
  }
  .services h2 { margin: 0 0 3px; font-size: 35px; font-weight: 700; line-height: 38px; }
  .services ul { list-style: none; }
  .services li { font-size: 29px; line-height: 35px; }
  .services li::before { content: "•"; font-size: 18px; vertical-align: 4px; }
  .booking {
    position: absolute;
    left: 150px;
    top: 940px;
    width: 584px;
    text-align: center;
    color: var(--ink);
    font-weight: 700;
  }
  .booking .prompt { display: block; font-size: 25px; line-height: 30px; }
  .booking .phone { display: block; font-size: 45px; line-height: 50px; margin-top: -3px; }
  .footer-wave {
    position: absolute;
    left: 0;
    top: 1020px;
    width: 934px;
    height: 180px;
  }
  .address {
    position: absolute;
    left: 150px;
    top: 1129px;
    width: 584px;
    text-align: center;
    color: var(--white);
    font-weight: 700;
    font-size: 24px;
    line-height: 29px;
  }
  .social {
    position: absolute;
    right: 12px;
    top: 1134px;
    width: 160px;
    text-align: center;
    color: var(--white);
    font-size: 13px;
    line-height: 1.2;
  }
  .social .handle { display: block; font-weight: 700; font-size: 15px; margin-top: 10px; }
</style>
</head>
<body>
<main class="flyer">
  <svg class="hero-art" viewBox="0 0 934 640" xmlns="http://www.w3.org/2000/svg">
    <defs>
      <linearGradient id="heroTone" x1="0" y1="0" x2="1" y2="1">
        <stop offset="0" stop-color="#e6eef6"/>
        <stop offset="0.5" stop-color="#f4f7fa"/>
        <stop offset="1" stop-color="#dbe6f0"/>
      </linearGradient>
    </defs>
    <path role="img" aria-label="Photo of a doctor in a white coat and tie with a stethoscope, writing with a pen"
          d="M0 0 H934 V200 C760 420 420 560 0 566 Z" fill="url(#heroTone)"/>
    <path d="M0 598 C440 594 780 456 934 212 L934 236 C790 482 450 622 0 632 Z" fill="var(--teal)"/>
    <path d="M0 564 C420 560 760 420 934 196 L934 214 C780 460 440 598 0 608 Z" fill="var(--sky-blue)"/>
  </svg>

  <div class="ribbon">NOW OPEN</div>
  <div class="brand-mark"></div>

  <h1 class="clinic-name">
    <span class="street">HALVORSEN AVENUE</span>
    <span class="word-medical">MEDICAL</span>
    <span class="word-clinic">CLINIC</span>
  </h1>

  <p class="headline">
    <span class="days">OPEN 6 DAYS A WEEK</span>
    <span class="walk-in">ACCEPTING WALK-IN PATIENTS</span>
  </p>

  <section class="services">
    <h2>SERVICES INCLUDES</h2>
    <ul>
      <li>Family Practice</li>
      <li>Cardiology Diagnostics</li>
      <li>Cardiac &amp; Vascular Surgical Consultation</li>
      <li>Ultrasound &amp; Vascular</li>
    </ul>
  </section>

  <p class="booking">
    <span class="prompt">TO BOOK APPOINTMENT, PLEASE CALL</span>
    <span class="phone">(416) 555-0148</span>
  </p>

  <svg class="footer-wave" viewBox="0 0 934 180" xmlns="http://www.w3.org/2000/svg">
    <path d="M0 56 C150 16 350 20 560 36 S820 60 934 48 V180 H0 Z" fill="var(--teal)"/>
    <path d="M0 80 C150 40 350 44 560 60 S820 84 934 70 V180 H0 Z" fill="var(--sky-blue)"/>
  </svg>

  <p class="address">2367 HALVORSEN AVENUE EAST UNIT 225<br>SCARBOROUGH, ONTARIO, K7T 2P4</p>

  <div class="social">join our community<span class="handle">@halvorsenclinic</span></div>
</main>
</body>
</html>
```